Mini Market Tavo Business Presentation Cards

We need presentation cards with a logo we already own designed at this website as well. We need the printing, delivery and sleek, modem design in harmony with our previous logo design.

Target Market(s)

Low, med and High income class.

Industry/Entity Type

Grocery Store

Contact Information for Business Card

Business logo (Mini Market Tavo), name: Esteban L. Morales/Lidia M. Paz/ Hugo Paz (those are the names for the different cards),
Address: Col. Lomas del Viento, carretera a Tela a 200mts del Centro Comunal. Puerto Cortés, Honduras.
Email: minimarkettavo@correo-ejemplo.hn
Teléfono: (504) 9731-5064

Font styles to use
Serif
Sans Serif

Requirements
Must have
• Business logo (Mini Market Tavo), person name, department,
• Address, phone number, email address.

```html
<!DOCTYPE html>
<html lang="es">
<head>
<meta charset="utf-8">
<title>Mini Market Tavo — Tarjetas de presentación</title>
<link rel="stylesheet" href="https://fonts.googleapis.com/css2?family=EB+Garamond:wght@400;500&family=Open+Sans:wght@400&display=swap">
<style>
  :root {
    --backdrop: #4a4a4a;
    --brand-red: #e23a22;
    --brand-green: #7ab648;
    --card-white: #f7f7f7;
    --ink-light: #ffffff;
    --ink-grey: #444444;
    --serif: "EB Garamond", Garamond, serif;
    --sans: "Open Sans", Arial, sans-serif;
  }
  * { margin: 0; padding: 0; box-sizing: border-box; }
  html, body {
    width: 1200px;
    height: 750px;
    overflow: hidden;
    background: var(--backdrop);
  }
  .card {
    position: absolute;
    top: 228px;
    width: 461px;
    height: 262px;
    overflow: hidden;
    background: var(--card-white);
  }
  .card--front { left: 124px; }
  .card--back { left: 618px; }

  .front-shape { position: absolute; inset: 0; }

  .person {
    position: absolute;
    left: 29px;
    top: 28px;
    color: var(--ink-light);
    font-family: var(--serif);
  }
  .person__name { font-size: 18px; font-weight: 500; line-height: 1.2; }
  .person__role { font-size: 13.5px; font-weight: 500; line-height: 1.3; }

  .address {
    position: absolute;
    left: 29px;
    top: 120px;
    width: 190px;
    color: var(--ink-light);
    font-family: var(--serif);
    font-size: 11.5px;
    line-height: 16px;
    font-style: normal;
  }

  .contact {
    position: absolute;
    left: 29px;
    top: 200px;
    list-style: none;
    color: var(--ink-light);
    font-family: var(--serif);
    font-size: 11.5px;
    line-height: 18.5px;
  }
  .contact li { display: flex; align-items: center; gap: 7px; }
  .contact svg { width: 12px; height: 12px; fill: var(--ink-light); flex: none; }

  .brand {
    position: absolute;
    display: flex;
    align-items: center;
  }
  .brand__name {
    font-family: var(--serif);
    font-weight: 400;
    color: var(--brand-red);
  }
  .brand__dot {
    border-radius: 50%;
    background: var(--brand-green);
  }
  .brand--front { left: 232px; top: 93px; gap: 9px; }
  .brand--front .brand__name { font-size: 23px; line-height: 1.05; width: 112px; text-align: left; }
  .brand--front .brand__dot { width: 78px; height: 78px; }

  .brand--back {
    left: 0;
    right: 0;
    top: 52px;
    flex-direction: column;
    gap: 10px;
  }
  .brand--back .brand__dot { width: 122px; height: 122px; }
  .brand--back .brand__name { font-size: 19px; }

  .website {
    position: absolute;
    left: 0;
    right: 0;
    top: 227px;
    text-align: center;
    font-family: var(--sans);
    font-size: 11px;
    letter-spacing: 0.38em;
    color: var(--ink-grey);
  }
</style>
</head>
<body>

<section class="card card--front" aria-label="Tarjeta, frente">
  <svg class="front-shape" viewBox="0 0 461 262" aria-hidden="true">
    <rect width="461" height="262" fill="var(--brand-red)"/>
    <circle cx="326" cy="131" r="135" fill="var(--brand-green)"/>
    <circle cx="326" cy="131" r="132" fill="var(--card-white)"/>
    <rect x="326" y="0" width="135" height="262" fill="var(--card-white)"/>
  </svg>

  <div class="person">
    <p class="person__name">Esteban L. Morales</p>
    <p class="person__role">CEO/Founder</p>
  </div>

  <address class="address">
    Col. Lomas del Viento,<br>
    carretera a Tela a 200mts<br>
    del Centro Comunal.<br>
    Puerto Cortés, Honduras.
  </address>

  <ul class="contact">
    <li>
      <svg viewBox="0 0 24 24" aria-hidden="true"><path d="M6.6 10.8a15.1 15.1 0 0 0 6.6 6.6l2.2-2.2a1 1 0 0 1 1-.25 11.4 11.4 0 0 0 3.6.57 1 1 0 0 1 1 1V20a1 1 0 0 1-1 1A17 17 0 0 1 3 4a1 1 0 0 1 1-1h3.5a1 1 0 0 1 1 1c0 1.25.2 2.45.57 3.57a1 1 0 0 1-.25 1z"/></svg>
      <span>(504) 9731-5064</span>
    </li>
    <li>
      <svg viewBox="0 0 24 24" aria-hidden="true"><path d="M2 5h20v14H2z M3.5 6.5 12 12.5l8.5-6" fill="none" stroke="#fff" stroke-width="0"/><path d="M2 5h20v1.6l-10 6.6-10-6.6z M2 8.9l10 6.6 10-6.6V19H2z"/></svg>
      <span>minimarkettavo@correo-ejemplo.hn</span>
    </li>
  </ul>

  <div class="brand brand--front">
    <span class="brand__name">Mini Market Tavo</span>
    <span class="brand__dot" aria-hidden="true"></span>
  </div>
</section>

<section class="card card--back" aria-label="Tarjeta, reverso">
  <div class="brand brand--back">
    <span class="brand__dot" aria-hidden="true"></span>
    <span class="brand__name">Mini Market Tavo</span>
  </div>
  <p class="website">www.sitiotavo.hn</p>
</section>

</body>
</html>
```